Corinnebelhoff.com

1. Conceptualization and designing of the site Homepage. The Homepage design will be completely customized and based on your design instructions (i.e. preferred colors, links to reference sites that you want us to take reference from if any etc) and the recently completed logo design.
2. Upon homepage design approval, based on it we will be creating the layout for the other 4 site inner pages (i.e. About page, Contact page, Services page, and Insights (publications, media).
3. Once all the inner page designs are approved, we will get the designs built (will make sure that the site is completely Responsive - works on all devices) within your provided WIX account.
4. We will add the static text and images provided by you to the Home page, About page, Contact page, and the Services page. For the 2 Insights sub-pages, we will add 1-2 sample Publications and Media entries.
once you confirm the total number of required entries for the 2 sub-pages, I will accordingly quote you on the same
5. Integration of a Contact form on the Contact page that will email the filled in details to your mail id.

```html
<!DOCTYPE html>
<html lang="en">
<head>
<meta charset="utf-8">
<title>Corinne Belhoff Consulting</title>
<link href="https://fonts.googleapis.com/css2?family=Poppins:wght@500;600;700&family=Roboto:wght@400;500;700&display=swap" rel="stylesheet">
<style>
:root{
  --blue:#1b9ce0;
  --green:#15933c;
  --green-bg:#199a3d;
  --orange:#f39200;
  --red:#e3140d;
  --ink:#222;
  --text:#555;
  --light-blue:#eaf5fc;
  --footer:#1f1f1f;
  --white:#fff;
}
*{margin:0;padding:0;box-sizing:border-box}
html,body{width:1200px;height:3437px;overflow:hidden}
body{position:relative;font-family:"Roboto",sans-serif;color:var(--text);background:var(--white)}
.abs{position:absolute}
.heading{font-family:"Poppins",sans-serif;font-weight:600;color:var(--ink);font-size:40px;line-height:1;letter-spacing:.5px}
.rule{position:absolute;height:3px;width:56px;background:var(--green)}
.btn{position:absolute;display:flex;align-items:center;justify-content:center;gap:10px;border-radius:30px;color:#fff;font-family:"Roboto",sans-serif;font-weight:700;font-size:16px;background:linear-gradient(90deg,var(--orange),var(--red));text-transform:uppercase}
.btn svg{width:15px;height:15px}
.btn-flow{position:relative;display:inline-flex}
.para{font-size:15px;line-height:27px;color:var(--text);margin-bottom:8px;letter-spacing:-.1px}

/* header */
.brand-mark{position:absolute;left:167px;top:10px;width:60px;height:60px;border-radius:50%;border:3px solid #333}
.brand-name{position:absolute;left:108px;top:74px;width:176px;text-align:center;font-family:"Poppins",sans-serif;font-weight:600;color:var(--blue);font-size:15px;line-height:16px}
.brand-name small{display:block;font-size:11px;letter-spacing:3px}
.top-mail{position:absolute;left:568px;top:18px;display:flex;align-items:center;gap:16px;font-size:17px;color:#333}
.social{position:absolute;top:19px;width:28px;height:28px;border-radius:50%;border:1.5px solid var(--blue)}
.nav-bar{position:absolute;left:347px;top:64px;width:613px;height:41px;background:var(--blue);clip-path:polygon(28px 0,100% 0,100% 100%,0 100%)}
.nav{position:absolute;left:392px;top:64px;height:41px;display:flex;align-items:center;color:#fff;font-size:16px}
.nav span.sep{margin:0 26px}
.call{position:absolute;left:936px;top:0;width:264px;height:105px;background:var(--green);clip-path:polygon(36px 0,100% 0,100% 100%,0 100%)}
.call-icon{position:absolute;left:972px;top:35px;width:38px;height:38px;border-radius:50%;background:var(--red);display:flex;align-items:center;justify-content:center}
.call-text{position:absolute;left:1018px;top:30px;color:#fff}
.call-text small{display:block;font-size:12.5px;font-weight:500}
.call-text b{font-size:21px;font-weight:700}

/* hero */
.hero{position:absolute;left:0;top:105px;width:1200px;height:631px;background:linear-gradient(160deg,#c9ced4 0%,#8e9aa6 40%,#5d6d7e 70%,#b9c1c8 100%)}
.hero-box{position:absolute;left:278px;top:307px;width:643px;height:258px;background:rgba(110,110,110,.55)}
.hero-title{position:absolute;left:278px;top:335px;width:643px;text-align:center;font-family:"Poppins",sans-serif;font-weight:700;font-size:58px;line-height:62px;color:#fff}

/* about */
.about-ring{position:absolute;left:116px;top:822px;width:430px;height:440px;border-radius:50%;border:4px solid #111;border-right-color:transparent;transform:rotate(-20deg)}
.about-photo{position:absolute;left:140px;top:846px;width:382px;height:382px;border-radius:50%;background:linear-gradient(135deg,#d7d2cb,#8b8378 60%,#5c5750)}
.about-portrait{position:absolute;left:374px;top:1124px;width:128px;height:128px;border-radius:50%;border:4px solid #fff;background:linear-gradient(160deg,#8d7a6a,#3b3331);box-shadow:0 0 0 2px #222}
.about-copy{position:absolute;left:597px;top:900px;width:492px}

/* services */
.services{position:absolute;left:0;top:1359px;width:1200px;height:493px;background:var(--light-blue)}
.card{position:absolute;top:1525px;width:470px;height:217px;background:#fff;border-right:3px solid var(--green);box-shadow:0 4px 12px rgba(0,0,0,.12)}
.card-img{position:absolute;left:0;top:0;width:226px;height:217px}
.card-icon{position:absolute;left:199px;top:77px;width:62px;height:62px;border-radius:50%;background:var(--blue);border:5px solid #cfe9f7;display:flex;align-items:center;justify-content:center}
.card-body{position:absolute;left:262px;top:0;width:200px;text-align:center}
.card-title{margin-top:30px;font-size:18px;font-weight:500;color:var(--ink)}
.card-text{margin-top:10px;font-size:14px;line-height:23px;color:var(--text)}
.card-link{margin-top:10px;font-size:14px;font-weight:700;color:var(--blue);display:flex;justify-content:center;align-items:center;gap:8px}

/* insights */
.insights-copy{position:absolute;left:127px;top:2052px;width:426px;text-align:justify}
.ins-photo{position:absolute;left:630px;top:1949px;width:477px;height:435px;background:linear-gradient(90deg,#e7e3da 0%,#7a3a25 35%,#5b2618 60%,#e3ddd2 100%)}
.frame-left{position:absolute;left:611px;top:2058px;width:4px;height:347px;background:var(--blue)}
.frame-bottom{position:absolute;left:611px;top:2401px;width:443px;height:4px;background:linear-gradient(90deg,var(--blue),var(--green))}
.frame-right{position:absolute;left:1050px;top:2384px;width:4px;height:21px;background:var(--green)}

/* contact */
.contact{position:absolute;left:0;top:2491px;width:1200px;height:558px;background:var(--green-bg)}
.field{position:absolute;background:#f4f4f4;border-radius:30px;color:#888;font-size:16px;padding-left:30px;display:flex;align-items:center}

/* footer */
.footer{position:absolute;left:0;top:3049px;width:1200px;height:388px;background:var(--footer)}
.f-col{position:absolute;top:3112px;color:#fff}
.f-col h4{font-size:17px;font-weight:700;margin-bottom:18px}
.f-col li{list-style:none;font-size:13.5px;line-height:32px}
.f-item{position:absolute;left:836px;color:#fff;font-size:13.5px;line-height:18px}
.f-item b{display:block;font-size:12px}
</style>
</head>
<body>

<header>
  <div class="brand-mark"></div>
  <div class="brand-name">CORINNE BELHOFF<small>CONSULTING</small></div>

  <div class="top-mail">
    <svg width="34" height="30" viewBox="0 0 34 30"><rect x="2" y="8" width="30" height="20" fill="none" stroke="#e8542a" stroke-width="2"/><path d="M2 8 L17 19 L32 8" fill="none" stroke="#e8542a" stroke-width="2"/><rect x="9" y="2" width="16" height="10" fill="#fff" stroke="#e8542a" stroke-width="1.5"/></svg>
    <span>info@corinnebelhoff.com.au</span>
  </div>
  <div class="social" style="left:868px"></div>
  <div class="social" style="left:905px"></div>

  <div class="nav-bar"></div>
  <nav class="nav">
    <span>Home</span><span class="sep">|</span>
    <span>About Us</span><span class="sep">|</span>
    <span>Insights</span><span class="sep">|</span>
    <span>Services</span><span class="sep">|</span>
    <span>Contact Us</span>
  </nav>

  <div class="call"></div>
  <div class="call-icon">
    <svg width="20" height="20" viewBox="0 0 24 24"><path d="M6.6 10.8a15.1 15.1 0 0 0 6.6 6.6l2.2-2.2c.3-.3.7-.4 1-.2 1.1.4 2.3.6 3.6.6.6 0 1 .4 1 1V20c0 .6-.4 1-1 1A17 17 0 0 1 3 4c0-.6.4-1 1-1h3.5c.6 0 1 .4 1 1 0 1.3.2 2.5.6 3.6.1.3 0 .7-.2 1z" fill="#fff"/></svg>
  </div>
  <div class="call-text"><small>Call Us Today</small><b>+1 888 888 8888</b></div>
</header>

<section class="hero" role="img" aria-label="Photo of consultants meeting around an office table"></section>
<div class="hero-box"></div>
<h1 class="hero-title">CORINNE BELHOFF<br>CONSULTING</h1>
<a class="btn" style="left:517px;top:480px;width:168px;height:47px">Get Started
  <svg viewBox="0 0 16 16"><circle cx="8" cy="8" r="8" fill="#fff"/><path d="M6 4.5 9.5 8 6 11.5" stroke="#e3140d" stroke-width="2" fill="none"/></svg></a>

<section class="about">
  <div class="about-ring"></div>
  <div class="about-photo" role="img" aria-label="Photo of a consultant reviewing documents with a couple"></div>
  <div class="about-portrait" role="img" aria-label="Portrait photo of the consultant"></div>
  <div class="rule" style="left:597px;top:832px"></div>
  <h2 class="heading abs" style="left:597px;top:848px">ABOUT US</h2>
  <div class="about-copy">
    <p class="para">Lorem ipsum dolor sit amet, consectetur adipiscing elit, sed do eiusmod tempor incididunt ut labore et dolore magna aliqua. Ut enim ad minim veniam, quis nostrud exercitation ullamco laboris nisi ut aliquip ex ea commodo consequat. Duis aute irure dolor in reprehenderit</p>
    <p class="para">Consectetur adipiscing elit, sed do eiusmod tempor incididunt ut labore et dolore magna aliqua enim ad minim veniam, quis nostrud exercitation ullamco laboris nisi ut aliquip ex ea commodo consequat. Duis aute irure dolor in reprehenderit in voluptate velit esse cillum dolored.</p>
    <p class="para">Bostrud exercitation ullamco laboris aliquip commodo consequat Duis aute irure dolor in reprehenderit in voluptate velit esse cillum.</p>
    <a class="btn btn-flow" style="width:168px;height:47px;margin-top:14px">Learn More
      <svg viewBox="0 0 16 16"><circle cx="8" cy="8" r="8" fill="#fff"/><path d="M6 4.5 9.5 8 6 11.5" stroke="#e3140d" stroke-width="2" fill="none"/></svg></a>
  </div>
</section>

<section class="services"></section>
<div class="rule" style="left:572px;top:1421px"></div>
<h2 class="heading abs" style="left:0;width:1200px;text-align:center;top:1437px">OUR SERVICES</h2>

<article class="card" style="left:112px">
  <div class="card-img" role="img" aria-label="Photo of two colleagues working at a laptop" style="background:linear-gradient(135deg,#8d8a86,#3a3633)"></div>
  <div class="card-icon"><svg width="26" height="26" viewBox="0 0 26 26" fill="none" stroke="#fff" stroke-width="1.6"><circle cx="8" cy="6" r="3"/><circle cx="18" cy="6" r="3"/><path d="M3 22v-7a4 4 0 0 1 8 0v7M15 22v-7a4 4 0 0 1 8 0v7"/></svg></div>
  <div class="card-body">
    <div class="card-title">Consulting Firm</div>
    <div class="card-text">Lorem ipsum dolor sit amet consectetur adipiscing elitsed do eiusmod tempor incididunt ut labore et</div>
    <div class="card-link">LEARN MORE <svg width="13" height="13" viewBox="0 0 16 16"><circle cx="8" cy="8" r="7" fill="none" stroke="#1b9ce0" stroke-width="2"/><path d="M6.5 5 9.5 8 6.5 11" stroke="#1b9ce0" stroke-width="2" fill="none"/></svg></div>
  </div>
</article>

<article class="card" style="left:615px">
  <div class="card-img" role="img" aria-label="Photo of a nurse writing on a clipboard" style="background:linear-gradient(135deg,#5f8fc2,#c8d7e6 60%,#e9ecef)"></div>
  <div class="card-icon"><svg width="26" height="26" viewBox="0 0 26 26" fill="none" stroke="#fff" stroke-width="1.6"><circle cx="13" cy="8" r="4"/><path d="M5 23v-4a8 8 0 0 1 16 0v4z"/><path d="M13 17v4M11 19h4"/></svg></div>
  <div class="card-body">
    <div class="card-title">Registered Nurses</div>
    <div class="card-text">Lorem ipsum dolor sit amet consectetur adipiscing elitsed do eiusmod tempor incididunt ut labore et</div>
    <div class="card-link">LEARN MORE <svg width="13" height="13" viewBox="0 0 16 16"><circle cx="8" cy="8" r="7" fill="none" stroke="#1b9ce0" stroke-width="2"/><path d="M6.5 5 9.5 8 6.5 11" stroke="#1b9ce0" stroke-width="2" fill="none"/></svg></div>
  </div>
</article>

<section class="insights">
  <div class="rule" style="left:127px;top:1983px"></div>
  <h2 class="heading abs" style="left:127px;top:2000px">INSIGHTS</h2>
  <div class="insights-copy">
    <p class="para">Lorem ipsum dolor sit amet, consectetur adipiscing elit, sed do eiusmod tempor incididunt ut labore et dolore magna aliqua. Ut enim ad minim veniam, quis nostrud exercitation ullamco laboris nisi ut aliquip ex ea commodo consequat.</p>
    <p class="para">Consectetur adipiscing elit, sed do eiusmod tempor incididunt ut labore et dolore magna aliqua. Ut enim ad minim veniam, quis nostrud exercitation ullamco laboris nisi ut aliquip ex ea commodo consequated Duis aute irure dolor.</p>
    <a class="btn btn-flow" style="width:159px;height:41px;font-size:15px;margin-top:12px">Learn More
      <svg viewBox="0 0 16 16"><circle cx="8" cy="8" r="8" fill="#fff"/><path d="M6 4.5 9.5 8 6 11.5" stroke="#e3140d" stroke-width="2" fill="none"/></svg></a>
  </div>

  <svg class="abs" style="left:1000px;top:1912px" width="140" height="116">
    <defs><pattern id="dots" width="16" height="16" patternUnits="userSpaceOnUse"><circle cx="4" cy="4" r="1.8" fill="#1b9ce0"/></pattern></defs>
    <rect x="0" y="0" width="140" height="32" fill="url(#dots)"/>
    <rect x="112" y="32" width="28" height="84" fill="url(#dots)"/>
  </svg>
  <div class="frame-left"></div>
  <div class="frame-bottom"></div>
  <div class="frame-right"></div>
  <div class="ins-photo" role="img" aria-label="Photo of the consultant standing before a wooden doorway between two flags"></div>
</section>

<section class="contact"></section>
<div class="rule" style="left:572px;top:2563px;background:#fff"></div>
<h2 class="heading abs" style="left:0;width:1200px;text-align:center;top:2585px;color:#fff">CONTAT US</h2>
<div class="field" style="left:105px;top:2666px;width:478px;height:61px">Name</div>
<div class="field" style="left:111px;top:2749px;width:478px;height:61px">Email Address</div>
<div class="field" style="left:111px;top:2829px;width:478px;height:61px">Phone Number</div>
<div class="field" style="left:611px;top:2665px;width:484px;height:225px;border-radius:24px;align-items:flex-start;padding-top:24px">Message</div>
<a class="btn" style="left:521px;top:2940px;width:157px;height:40px;font-size:15px">Submit Now
  <svg viewBox="0 0 16 16"><circle cx="8" cy="8" r="8" fill="#fff"/><path d="M6 4.5 9.5 8 6 11.5" stroke="#e3140d" stroke-width="2" fill="none"/></svg></a>

<footer class="footer"></footer>
<div class="abs" style="left:180px;top:3148px;width:80px;height:80px;border-radius:50%;border:3px solid #ddd"></div>
<div class="abs" style="left:100px;top:3234px;width:240px;text-align:center;font-family:'Poppins',sans-serif;font-weight:600;color:var(--blue);font-size:21px;line-height:22px">CORINNE BELHOFF<span style="display:block;font-size:15px;letter-spacing:4px">CONSULTING</span></div>

<div class="f-col" style="left:417px">
  <h4>Quick Links</h4>
  <ul><li>Home</li><li>About Us</li><li>Insights</li><li>Services</li><li>Contact us</li></ul>
</div>
<div class="f-col" style="left:603px">
  <h4>About Company</h4>
  <ul><li>Terms of Use</li><li>Terms &amp; Condition</li><li>News</li><li>Contact Us</li><li>FAQ</li></ul>
</div>
<div class="f-col" style="left:836px"><h4>Contact Us</h4></div>

<svg class="abs" style="left:836px;top:3160px" width="10" height="14" viewBox="0 0 10 14"><path d="M5 0a5 5 0 0 1 5 5c0 4-5 9-5 9S0 9 0 5a5 5 0 0 1 5-5z" fill="#1b9ce0"/><circle cx="5" cy="5" r="2" fill="#1f1f1f"/></svg>
<div class="f-item" style="left:858px;top:3155px"><b>Location</b>Maple Falls, Ohio, United States</div>
<svg class="abs" style="left:836px;top:3214px" width="13" height="13" viewBox="0 0 24 24"><path d="M6.6 10.8a15.1 15.1 0 0 0 6.6 6.6l2.2-2.2c.3-.3.7-.4 1-.2 1.1.4 2.3.6 3.6.6.6 0 1 .4 1 1V20c0 .6-.4 1-1 1A17 17 0 0 1 3 4c0-.6.4-1 1-1h3.5c.6 0 1 .4 1 1 0 1.3.2 2.5.6 3.6.1.3 0 .7-.2 1z" fill="#1b9ce0"/></svg>
<div class="f-item" style="left:858px;top:3209px"><b>Phone</b>+1 888 888 8888</div>
<svg class="abs" style="left:836px;top:3265px" width="15" height="11" viewBox="0 0 15 11"><rect width="15" height="11" fill="#1b9ce0"/><path d="M0 0 7.5 6 15 0" stroke="#1f1f1f" stroke-width="1.5" fill="none"/></svg>
<div class="f-item" style="left:858px;top:3258px"><b>Email</b>info@corinnebelhoffconsulting.com</div>

<div class="abs" style="left:1130px;top:3294px;width:38px;height:38px;border-radius:50%;background:linear-gradient(135deg,var(--orange),var(--red));display:flex;align-items:center;justify-content:center">
  <svg width="14" height="14" viewBox="0 0 14 14"><path d="M2 9.5 7 4.5 12 9.5" stroke="#fff" stroke-width="2" fill="none"/></svg>
</div>

<div class="abs" style="left:112px;top:3364px;width:976px;height:1px;background:#444"></div>
<div class="abs" style="left:0;top:3394px;width:1200px;text-align:center;color:#fff;font-size:15px">2024 Copyright -Corinne Belhoff Consulting &nbsp;| All Rights Reserved</div>

</body>
</html>
```